Counseling Practice Business Card

I need a professional looking business card incorporating my new logo that was just completed. Card needs to incorporate my name and title, description of my specialty, my address, my phone number, my fax number, my email and my website URL. I need to be able to choose design on/with different paper colors and textures.
I do not have a lot of business card ideas so I am open to anything but I want bold,sharp, clear card without additional designs other than my logo (see attached file info). I am open to different color backgrounds or paper colors including black. I do not like traditional brackets around area codes in phone number or dashes between numbers in phone number. Am open to other ways of presenting including periods between numbers as appropriate. I do not know enough to know what I like yet but I want card to coordinate and work together with my logo. My practice emphasizes natural mental health interventions so any use of color (with background paper color or the blue and green in my logo) that elicits nature is nice. In addition to black, any natural brown or wood looking background might be desirable also. Most of the offerings so far look very similar and boring.

Target Market(s)

Potential therapy clients and other professionals

Contact Information for Business Card

Card information:
Marcus T. Whitfield, Ph.D.
Licensed Clinical Psychologist
Integrative Health Coach
4812 Ferndale Pkwy NW
Suite 730
Duluth, GA 30096
(770) 555-0142 phone
(770) 555-0186 fax
drmarcuswhitfield@kelvora.com
pathbloomcounseling.com

Font styles to use
Serif
Sans Serif
Other font styles liked:
• anything that you think looks crisp, clear and easily readable

Requirements
Must have
• Any color used should coordinate with my logo design (see attached files).
• Card should be printed horizontally so top and bottom are longest sides of rectangle.
• Background color or paper color should complement and highlight logo. Do not like a white background. black, grey, brown or any color my logo would blend well with.
Nice to have
• I would like designer to utilize color to highlight letters/name or phone-fax-web symbols.
• Bottom edge of card could be highlighted if appropriate to an idea.
Should not have
• I would NOT want the card to have a pure white background at all.
• No clear cards.
• Cards should be oriented with long sides on bottom and top, NOT sides. DO NOT LIKE THIS THIN TALL ORIENTATION.

```html
<!DOCTYPE html>
<html lang="en">
<head>
<meta charset="utf-8">
<title>Pathbloom Counseling – Business Card</title>
<link href="https://fonts.googleapis.com/css2?family=Open+Sans:wght@400;600&display=swap" rel="stylesheet">
<style>
  :root {
    --backdrop: #5a5a5c;
    --card-stock: #f5f2ea;
    --brand-blue: #1f6fb5;
    --brand-green: #1b6b3a;
    --back-blue: #2f7bc4;
    --back-pattern: #3a86cc;
    --text-dark: #3a3a3a;
    --divider: #b9b9b9;
  }
  * { box-sizing: border-box; margin: 0; padding: 0; }
  html, body { width: 1200px; height: 802px; overflow: hidden; }
  body {
    background: var(--backdrop);
    font-family: "Open Sans", Arial, sans-serif;
    position: relative;
  }
  .card {
    position: absolute;
    top: 274px;
    width: 443px;
    height: 265px;
    box-shadow: 0 3px 8px rgba(0,0,0,.45);
    overflow: hidden;
  }
  .card--front { left: 136px; background: var(--card-stock); }
  .card--back { left: 624px; background: var(--back-blue); }

  .brand {
    position: absolute;
    color: var(--brand-blue);
    font-weight: 600;
    text-align: center;
    line-height: 1;
  }
  .brand__name { display: block; font-size: 31px; letter-spacing: .3px; }
  .brand__tag { display: block; font-size: 10px; font-weight: 400; letter-spacing: 9px; margin-top: 6px; padding-left: 9px; }
  .card--front .brand { left: 18px; top: 104px; width: 164px; }

  .divider {
    position: absolute;
    left: 198px; top: 63px;
    width: 1px; height: 146px;
    background: linear-gradient(to bottom, transparent, var(--divider) 15%, var(--divider) 85%, transparent);
  }

  .details { position: absolute; left: 215px; top: 51px; color: var(--text-dark); }
  .details__name {
    font-size: 14px; font-weight: 600; letter-spacing: .2px;
    white-space: nowrap; line-height: 19px;
  }
  .details__name .first, .details__name .cred { color: var(--brand-blue); }
  .details__name .last { color: var(--brand-green); }
  .details__title { font-size: 12px; line-height: 16px; margin-top: 0; }
  .contact { list-style: none; margin-top: 6px; font-size: 12px; line-height: 15.5px; }
  .contact li { display: flex; align-items: center; gap: 3px; white-space: nowrap; }
  .contact svg { width: 10px; height: 10px; fill: var(--brand-blue); flex: none; }
  .address { font-style: normal; font-size: 12px; line-height: 15.5px; margin-top: 8px; }

  .pattern { position: absolute; inset: 0; background: var(--back-pattern); opacity: .35; }
  .card--back .brand { color: #ffffff; left: 196px; width: 122px; top: 113px; }
  .card--back .brand__name { font-size: 19px; }
  .card--back .brand__tag { font-size: 6px; letter-spacing: 4px; margin-top: 3px; padding-left: 4px; }
</style>
</head>
<body>
  <section class="card card--front" aria-label="Business card front">
    <div class="brand">
      <span class="brand__name">Pathbloom</span>
      <span class="brand__tag">COUNSELING</span>
    </div>
    <div class="divider"></div>
    <div class="details">
      <p class="details__name"><span class="first">MARCUS</span> <span class="last">T. WHITFIELD</span><span class="cred">, PH.D.</span></p>
      <p class="details__title">Licensed Clinical Psychologist /<br>Integrative Health Coach</p>
      <ul class="contact">
        <li><svg viewBox="0 0 10 10" aria-hidden="true"><path d="M1 3.5C1 2 3 1.5 5 1.5S9 2 9 3.5L7.5 4 7 3H3L2.5 4ZM2.5 5h5l1 3.5h-7Z"/></svg>770. 555.0142</li>
        <li><svg viewBox="0 0 10 10" aria-hidden="true"><path d="M3 1h4v2H3ZM1 3.5h8V7H7.5V6h-5v1H1ZM3 6.5h4V9H3Z"/></svg>770. 555.0186</li>
        <li><svg viewBox="0 0 10 10" aria-hidden="true"><path d="M1 2h8v.8L5 5.5 1 2.8ZM1 3.8l4 2.7 4-2.7V8H1Z"/></svg>drmarcuswhitfield@kelvora.com</li>
        <li><svg viewBox="0 0 10 10" aria-hidden="true"><circle cx="5" cy="5" r="4.2"/></svg>pathbloomcounseling.com</li>
      </ul>
      <address class="address">4812 Ferndale Pkwy NW<br>Suite 730 Duluth, GA 30096</address>
    </div>
  </section>

  <section class="card card--back" aria-label="Business card back">
    <div class="pattern" role="img" aria-label="Faint repeating brand-name pattern across the blue background"></div>
    <div class="brand">
      <span class="brand__name">Pathbloom</span>
      <span class="brand__tag">COUNSELING</span>
    </div>
  </section>
</body>
</html>
```